Anzeigengestaltung für Dietrich Wollmann GmbH
Zielgruppe
Hydraulikmontagen, Aggregatebau
Aufgabenstellung
Wir sind vor 1 Jahr in eine neue Region gezogen und möchten uns hier bekannt machen.
Die Anzeige sollte direkt mit einem optischen Highlight ins Auge springen.
Was wir machen finden Sie auf:www.wollmann-technologies.de Schwerpunkt der Anzeige liegt auf der Hydraulik!!
Hauptsächlich wollen wir regional Werbung machen für Montagen, REparaturen, Aggregatebau

```html
<!DOCTYPE html>
<html lang="de">
<head>
<meta charset="utf-8">
<title>Dietrich Wollmann GmbH – Hydraulikservice</title>
<link href="https://fonts.googleapis.com/css2?family=Nunito+Sans:wght@400;600;700;800;900&family=Righteous&display=swap" rel="stylesheet">
<style>
  :root {
    --gold: #f2b700;
    --gold-dark: #d9a300;
    --blue: #2a6799;
    --red: #c0161c;
    --ink: #333333;
    --paper: #ffffff;
    --band-light: #84a3c6;
    --band-dark: #3a6d9c;
  }
  html, body {
    margin: 0;
    padding: 0;
    width: 848px;
    height: 1200px;
    overflow: hidden;
    background: var(--paper);
  }
  .ad {
    position: relative;
    width: 848px;
    height: 1200px;
    background: var(--paper);
    font-family: "Nunito Sans", sans-serif;
    color: var(--ink);
  }
  .hero {
    position: absolute;
    left: 0; top: 0;
    width: 848px; height: 536px;
    background:
      radial-gradient(ellipse at 30% 35%, #cfe6f2 0%, rgba(160,200,222,0.6) 25%, rgba(40,80,110,0) 55%),
      radial-gradient(ellipse at 80% 40%, #b9d8ea 0%, rgba(120,170,200,0.5) 25%, rgba(30,60,90,0) 55%),
      linear-gradient(180deg, #1d3346 0%, #3f7391 45%, #6aa3c0 70%, #16232e 100%);
  }
  .hero-title {
    position: absolute;
    left: 0; right: 0; top: 28px;
    text-align: center;
    padding-left: 40px;
    font-family: "Righteous", sans-serif;
    font-size: 33px;
    letter-spacing: 0.5px;
    color: #ffffff;
    text-shadow: 0 0 2px #1b2a36, 1px 1px 0 #1b2a36, -1px -1px 0 #1b2a36;
    margin: 0;
  }
  .gold-rule {
    position: absolute;
    left: 0; top: 536px;
    width: 848px; height: 14px;
    background: linear-gradient(90deg, var(--gold-dark), var(--gold), var(--gold-dark));
  }
  .headline {
    position: absolute;
    left: 66px; top: 590px;
    margin: 0;
    color: var(--red);
    font-weight: 900;
    font-size: 39px;
    line-height: 46px;
    text-transform: uppercase;
    transform: rotate(-5deg);
    transform-origin: left top;
  }
  .headline span { display: block; }
  .headline .indent { padding-left: 88px; }
  .services {
    position: absolute;
    right: 43px; top: 714px;
    width: 780px;
    text-align: right;
    margin: 0; padding: 0;
    list-style: none;
    font-size: 22px;
    line-height: 30px;
    font-weight: 400;
  }
  .services li { margin-bottom: 17px; }
  .services li.tight { margin-bottom: 14px; }
  .hl-gold { color: var(--gold); font-weight: 800; font-size: 27px; }
  .hl-blue { color: var(--blue); font-weight: 800; font-size: 27px; }
  .hl-dark { color: var(--ink); font-weight: 800; font-size: 21px; }
  .hl-italic { color: var(--gold); font-weight: 800; font-style: italic; font-size: 29px; }
  .hl-small-gold { color: var(--gold); font-weight: 800; font-size: 21px; }
  .hl-big-gold { color: var(--gold); font-weight: 800; font-size: 33px; }
  .brand {
    position: absolute;
    left: 34px; top: 1036px;
    display: flex;
    align-items: center;
    gap: 12px;
  }
  .brand-dot {
    width: 40px; height: 40px;
    border-radius: 50%;
    background: var(--gold);
  }
  .brand-name {
    font-size: 30px;
    font-weight: 700;
    color: var(--ink);
    line-height: 1;
  }
  .contact {
    position: absolute;
    right: 22px; top: 1076px;
    text-align: right;
    font-size: 13.5px;
    line-height: 22.5px;
    color: var(--ink);
    margin: 0;
    font-style: normal;
  }
  .footer-band {
    position: absolute;
    left: 0; bottom: 0;
    width: 848px; height: 57px;
    background: linear-gradient(90deg, var(--band-light), var(--band-dark));
    color: #ffffff;
    font-weight: 800;
    font-size: 21.5px;
    line-height: 57px;
    text-align: center;
  }
</style>
</head>
<body>
<main class="ad">
  <div class="hero" role="img" aria-label="Foto: vier Manometer mit Absperrventilen an einem Hydraulikprüfstand, in Blautönen"></div>
  <h2 class="hero-title">WIR KÖNNEN MIT IHREM DRUCK UMGEHEN</h2>
  <div class="gold-rule"></div>

  <h1 class="headline">
    <span>Ihr Hydraulikservice</span>
    <span class="indent">für die Region</span>
  </h1>

  <ul class="services">
    <li><span class="hl-gold">Projektierung</span> und <span class="hl-gold">Auslegung</span> von hydraulischen<br>Antriebselementen und Steuerelementen.</li>
    <li><span class="hl-blue">Hydraulikaggregatebau</span> bis zu einer Antriebsleistung von<br>P=250KW und einem Gesamtgewicht von 20ton</li>
    <li class="tight"><span class="hl-dark">Montage-, Installation-</span> und <span class="hl-dark">Reparaturdienstleistung</span> <span class="hl-italic">weltweit.</span></li>
    <li class="tight">Sicherheitstechnische <span class="hl-blue">Prüfungen</span> und <span class="hl-blue">Dokumentationen</span></li>
    <li><span class="hl-small-gold">Ersatzteilverkauf/Komponentenverkauf</span> und <span class="hl-big-gold">Beratung</span></li>
  </ul>

  <div class="brand">
    <div class="brand-dot"></div>
    <div class="brand-name">Dietrich Wollmann</div>
  </div>

  <address class="contact">
    Dietrich Wollmann GmbH<br>
    Am Talweg 12 | 35799 Mühlbach | Telefon: 01234 – 56789-0<br>
    Fax: 01234 – 56789-68 | Email: info(at)wollmann-technologies.de
  </address>

  <div class="footer-band">Informieren sich sich unter www.wollmann-hydraulik.de</div>
</main>
</body>
</html>
```